Catchy design für Verpackungsaufkleber für Rasensamenmischungen gesucht
Zielgruppe
Wir sind ein Onlineversandhandel (kaufwelt und onlineshop) für Rasensamenprodukte. Zielgruppe sind Eigenheimbesitzer mit Garten. 70% männlich. Die brand heisst 'wiesgrund'
Aufgabenstellung
Ich benötige Verpackungsaufkleber DINA5 und DINA6 für 2 Rasensamenmischungen in insgesamt 7 Größenvarianten. Am Besten wäre es vmtl., zunächst 2 unterschiedliche designs für Sport&Spiel und Schatten zu entwerfen und danach dann in die verschiedenen Größen kopieren.
Hinweise fürs design
Alle Rasensamen-Designs auf Kaufwelt https://www.kaufwelt-beispiel.de/s?k=rasensamen&crid=7QZRT2LWK41XB&sprefix=rasensamen%2Caps%2C248&ref=nb_sb_noss_1 sehen ähnlich aus (und langweilig), und ich überlege, wie man sich auf von den Farben, dem Design und der Schrift in erfrischender Weise abheben kann. Vielleicht mit diesem humorvollen und modernen Stil, mit auffälligen, witzigen Schriftarten und einem coolen Spruch wie „Dein Garten, dein Spielfeld!“, „Wächst, wo andere aufgeben.“ oder „Grün kann jeder – wir machen’s besser.“ GERNE AUCH EIGENE COOLE SPRÜCHE (analog Lorenzo fiore https://lorenzo-fiore-beispiel.de/pizzen/#DUE)
Farbenpalette:
Mutige Farben wie Gelb, Orange, Blau oder Lila, kombiniert mit Akzenten in Grün.
Beispiel: Ein sonniges Gelb mit einem dunklen, satten Grün für den Kontrast.
Illustrationen:
Comicartige Icons: z. B. spielende Kinder, ein Hund oder ein Fußball.
Vereinfachte Symbole wie Grashalme, Fußabdrücke oder eine Schaukel.
Layout:
Ein großflächiger Schriftzug in der Mitte, um die Botschaft sofort zu vermitteln.
Ein asymmetrisches Design, das Aufmerksamkeit erregt, ähnlich wie bei Lorenzo Fiore.
Hintergrundmuster:
Geometrische Formen, stilisierte Grashalme oder spielerische Muster.
Ein dynamisches Muster wie gestrichelte Linien oder Punkte, um Bewegung zu suggerieren.
Hersteller- und sontige Angaben für das Etikett, siehe die beiden .Pdfs im Anhang

```html
<!DOCTYPE html>
<html lang="de">
<head>
<meta charset="utf-8">
<title>Wiesgrund – Sport- &amp; Spiel-Rasensamen Etikett</title>
<link rel="stylesheet" href="https://fonts.googleapis.com/css2?family=Anton&family=Roboto+Condensed:wght@400;500;700;800&display=swap">
<style>
  :root {
    --label-black: #262626;
    --paper-white: #ffffff;
    --accent-green: #8cc63f;
    --grass-dark: #2f6e1f;
    --grass-mid: #4f9a2c;
    --grass-light: #7cbf3e;
    --text-dark: #1c1c1c;
    --page-bg: #ffffff;
  }
  * { box-sizing: border-box; margin: 0; padding: 0; }
  html, body {
    width: 1200px; height: 1200px; overflow: hidden;
    background: var(--page-bg);
    font-family: "Roboto Condensed", "Arial Narrow", sans-serif;
  }
  .label {
    position: absolute; left: 210px; top: 50px;
    width: 780px; height: 1100px;
    background: var(--label-black);
    overflow: hidden;
  }
  .label-art { position: absolute; inset: 0; }
  .brand-name {
    position: absolute; left: 175px; width: 423px; top: 26px;
    text-align: center;
    font-weight: 500; font-size: 96px; line-height: 1;
    color: var(--accent-green); letter-spacing: -1px;
  }
  .net-weight {
    position: absolute; left: 640px; top: 50px;
    font-weight: 800; font-size: 50px; line-height: 1;
    color: var(--paper-white);
  }
  .product-type {
    position: absolute; left: 100px; width: 580px; top: 806px;
    text-align: center; color: var(--paper-white);
    font-weight: 800; font-size: 33px; line-height: 34px;
  }
  .info-panel {
    position: absolute; left: 72px; width: 643px; top: 945px;
    text-align: center;
  }
  .certified {
    color: var(--accent-green); font-weight: 800; font-size: 22px;
    line-height: 1;
  }
  .benefits {
    list-style: none; display: flex; justify-content: center; gap: 14px;
    margin-top: 14px; color: var(--text-dark);
    font-weight: 500; font-size: 20px; line-height: 1;
  }
  .benefits li { display: flex; align-items: center; gap: 5px; }
  .benefits svg { width: 22px; height: 20px; }
  .storage-note {
    margin-top: 14px; color: var(--text-dark);
    font-weight: 400; font-size: 15px; line-height: 22px;
  }
</style>
</head>
<body>
  <div class="label">
    <svg class="label-art" width="780" height="1100" viewBox="0 0 780 1100">
      <defs>
        <linearGradient id="grass" x1="0" y1="0" x2="1" y2="1">
          <stop offset="0" stop-color="var(--grass-light)"/>
          <stop offset="0.5" stop-color="var(--grass-mid)"/>
          <stop offset="1" stop-color="var(--grass-dark)"/>
        </linearGradient>
      </defs>
      <polygon class="brand-panel" fill="var(--paper-white)"
        points="175,0 598,0 598,140 585,146 570,141 552,150 530,144 505,152 480,146 455,154 430,148 405,155 380,150 350,158 325,152 300,160 275,154 250,160 225,153 200,158 186,150 175,156"/>
      <g class="headline" role="img" aria-label="Schriftzug mit Rasen-Fototextur gefüllt" fill="url(#grass)" font-family="Anton, Impact, sans-serif">
        <text x="133" y="368" font-size="214" textLength="516" lengthAdjust="spacingAndGlyphs">DEIN</text>
        <text x="133" y="488" font-size="125" textLength="516" lengthAdjust="spacingAndGlyphs">GARTEN</text>
        <text x="133" y="688" font-size="213" textLength="516" lengthAdjust="spacingAndGlyphs">DEIN</text>
        <text x="122" y="782" font-size="94" textLength="538" lengthAdjust="spacingAndGlyphs">SPIELFELD!</text>
      </g>
      <polygon class="info-panel-bg" fill="var(--paper-white)"
        points="72,918 95,910 120,916 150,906 180,912 210,904 245,910 280,903 315,909 350,902 390,908 425,901 460,907 500,900 540,906 580,899 620,905 660,898 700,904 715,900 715,1100 72,1100"/>
      <g class="quality-badge" transform="translate(665 886)">
        <polygon fill="var(--accent-green)"
          points="0,-68 10,-55 22,-64 27,-49 41,-54 40,-39 55,-40 48,-26 62,-22 51,-12 64,-4 51,5 61,15 47,20 54,33 39,34 41,49 27,45 24,60 12,52 4,66 -5,53 -16,64 -21,49 -35,56 -35,41 -50,44 -45,29 -60,26 -49,15 -62,6 -50,-3 -60,-14 -46,-19 -53,-32 -38,-33 -42,-48 -28,-44 -24,-59 -12,-50"/>
        <g transform="rotate(10)" fill="var(--text-dark)" font-family="'Roboto Condensed', sans-serif" font-weight="800" font-size="19" text-anchor="middle">
          <text x="0" y="-4">PREMIUM</text>
          <text x="0" y="18">QUALITÄT</text>
        </g>
      </g>
    </svg>

    <div class="brand-name">Wiesgrund</div>
    <div class="net-weight">1kg</div>
    <p class="product-type">SCHNELLKEIMENDE SPORT-<br>&amp; SPIEL-RASENSAMEN</p>

    <div class="info-panel">
      <p class="certified">ZERTIFIZIERTES SAATGUT MADE IN GERMANY</p>
      <ul class="benefits">
        <li><svg viewBox="0 0 22 20"><path d="M2 11 L8 17 L20 2" fill="none" stroke="var(--accent-green)" stroke-width="3"/></svg>SCHNELLKEIMEND</li>
        <li><svg viewBox="0 0 22 20"><path d="M2 11 L8 17 L20 2" fill="none" stroke="var(--accent-green)" stroke-width="3"/></svg>TROCKENRESISTENT</li>
        <li><svg viewBox="0 0 22 20"><path d="M2 11 L8 17 L20 2" fill="none" stroke="var(--accent-green)" stroke-width="3"/></svg>MÄHROBOTERGEEIGNET</li>
      </ul>
      <p class="storage-note">Trocken und kühl lagern, um Schimmelbildung zu vermeiden.<br>Lagern Sie die Samen außerhalb der Reichweite von Kindern und Haustieren.</p>
    </div>
  </div>
</body>
</html>
```